label A4 format for transparant dog food (dehydrated) bag 10 kg

For our dehydrated dog food in transparent bags we need a coloured label, A4 format.
See our product online :
https://www.kopzaal.example/nl/p/velderkamp-mix-toblin-pr-10-kg-gedehydrateerde-verse-voeding-voor-honden/9200000018265394/

We have a basic concept but it needs to worked out by a professional designer (see attached :etiket ontwerp A4 1.pdf).

Basic concept

 General : a vintage aspect
 A basic background colour (see attached :etiket ontwerp A4 1.pdf). Please show a few different colours
 Only 1 logo (in the basic concept we used both logo’s but in the definite label, only 1 should be used; we do not know which is the better one)
 N° 1 is the name of the First variety of our product (we used the nr 5 logo of morvette)
 Tripe, rice, vegetables …. (composition of dog food)
 Superb fresh …..text
 A vintage image with an inspirational text : see attached
 User instructions : in simple drawings
 At the bottom the admin information : websiteadres, emailadres, telephone, vat nr etc.
 …………

Target Market(s)

dog owners who want a 100 % natural dog food without fillers etc.

Industry/Entity Type

Online

Logo Text

Velderkamp dehydrated dog food label A4 format

Font styles to use
Serif
Decorative

Requirements
Must have
• attractive design for dog food buyers , inspirational text concerning dogs
• vintage aspect, ecological aspect

```html
<!DOCTYPE html>
<html lang="nl">
<head>
<meta charset="utf-8">
<title>Velderkamp – Superb Fresh Dog Food labels</title>
<link rel="stylesheet" href="https://fonts.googleapis.com/css2?family=Cinzel+Decorative:wght@400;700&family=Libre+Baskerville:ital,wght@0,400;0,700;1,400&display=swap">
<style>
  :root{
    --page:#ffffff;
    --cream:#efe3c6;
    --cream-deep:#e6d7b4;
    --card:#e4d3ae;
    --card-edge:#d3bf95;
    --orange:#c77a24;
    --crimson:#a9444f;
    --teal:#4f8a7d;
    --slate:#5f7b8c;
    --paper:#e9dec3;
    --navy:#1f3a4b;
    --red:#a42a2b;
    --rust:#b0443a;
  }
  html,body{margin:0;padding:0;overflow:hidden;background:var(--page)}
  .canvas{position:relative;width:1200px;height:1200px;overflow:hidden;background:var(--page)}
  .defs{position:absolute;width:0;height:0}

  .label{
    position:absolute;width:374px;height:528px;overflow:hidden;
    background:var(--bg);
    --ink:var(--cream);
    --ribbon:var(--cream-deep);
    --badge:var(--cream);
    --badge-ink:var(--bg);
    --band:var(--cream-deep);
    --band-ink:var(--bg);
    --note:var(--rust);
    --sweep:var(--cream);
    color:var(--ink);
    font-family:"Libre Baskerville",Georgia,serif;
  }
  .label::after{
    content:"";position:absolute;inset:0;pointer-events:none;
    background:
      radial-gradient(ellipse at 30% 20%,rgba(255,255,255,.10),transparent 55%),
      radial-gradient(ellipse at 75% 70%,rgba(255,255,255,.08),transparent 50%),
      radial-gradient(ellipse at center,transparent 55%,rgba(0,0,0,.14) 100%);
  }
  .label--orange{--bg:var(--orange);left:23px;top:35px}
  .label--crimson{--bg:var(--crimson);left:413px;top:35px}
  .label--teal{--bg:var(--teal);left:804px;top:35px}
  .label--slate{--bg:var(--slate);left:202px;top:604px}
  .label--paper{
    --bg:var(--paper);left:604px;top:604px;
    --ink:var(--navy);--ribbon:var(--red);--badge:var(--cream);
    --badge-ink:var(--red);--band:var(--navy);--band-ink:var(--cream);--note:var(--cream);
    --sweep:var(--red);
  }

  .ribbon{position:absolute;left:10px;top:0;width:94px;height:182px}
  .ribbon path{fill:var(--ribbon)}
  .badge{position:absolute;left:25px;top:50px;width:112px;height:112px}
  .badge .disc{fill:var(--badge)}
  .badge .ring{fill:none;stroke:var(--badge-ink);stroke-width:2}
  .badge text{fill:var(--badge-ink);font-family:"Libre Baskerville",Georgia,serif;font-weight:700}
  .badge .arc{font-size:12.5px;letter-spacing:.5px}
  .badge .variety{font-size:27px}

  .brand{
    position:absolute;left:184px;top:80px;margin:0;
    font-family:"Libre Baskerville",Georgia,serif;font-weight:700;font-size:19px;
    color:var(--ink);display:flex;align-items:center;gap:7px;
  }
  .brand::before{content:"";width:9px;height:9px;border-radius:50%;background:var(--ink)}

  .sweep{position:absolute;left:0;top:0;width:374px;height:528px;pointer-events:none;fill:var(--sweep)}

  .headline{position:absolute;left:26px;top:194px;width:330px;margin:0;font-weight:400;color:var(--ink);
    font-variant-ligatures:none;font-feature-settings:"liga" 0,"dlig" 0}
  .headline .main{display:block;font-family:"Cinzel Decorative",Georgia,serif;font-size:34px;line-height:1;letter-spacing:.5px;white-space:nowrap}
  .headline .main b{font-size:48px;font-weight:400}
  .headline .sub{display:block;text-align:right;margin-top:0;font-family:"Cinzel Decorative",Georgia,serif;font-size:25px;line-height:1.1;white-space:nowrap}
  .because{position:absolute;left:150px;top:270px;margin:0;font-size:11px;color:var(--ink)}

  .card{
    position:absolute;left:102px;top:300px;width:184px;height:112px;
    transform:rotate(-4deg);
    background:linear-gradient(135deg,var(--card),var(--card-edge));
    box-shadow:0 1px 3px rgba(0,0,0,.18);
  }

  .band{position:absolute;left:0;top:436px;width:374px;height:70px;background:var(--band)}
  .steps{position:absolute;left:0;top:2px;width:374px;height:44px;color:var(--band-ink);fill:var(--band-ink)}
  .steps text{font-family:"Libre Baskerville",Georgia,serif;font-size:15px}
  .instructions{position:absolute;left:0;top:50px;width:374px;margin:0;text-align:center;font-size:10.5px;color:var(--note)}
</style>
</head>
<body>
<main class="canvas">

  <svg class="defs" aria-hidden="true">
    <defs>
      <path id="arc-top" d="M19,60 A41,41 0 0 1 101,60"/>
      <path id="arc-bottom" d="M10,60 A50,50 0 0 0 110,60"/>
      <symbol id="icon-bowl" viewBox="0 0 24 16"><path d="M1 5 H23 Q22 15 12 15 Q2 15 1 5Z" fill="currentColor"/></symbol>
      <symbol id="icon-jug" viewBox="0 0 20 24"><path d="M5 2 H14 L13 5 Q18 9 16 21 Q15 23 12 23 H6 Q3 23 3 20 Q2 10 6 5Z" fill="currentColor"/><path d="M3 9 Q-1 12 3 16" fill="none" stroke="currentColor" stroke-width="1.6"/></symbol>
      <symbol id="icon-spoon" viewBox="0 0 24 24"><path d="M4 20 L18 4" stroke="currentColor" stroke-width="2" stroke-linecap="round"/><ellipse cx="19" cy="3.5" rx="3" ry="2" transform="rotate(-45 19 3.5)" fill="currentColor"/></symbol>
      <symbol id="icon-steam" viewBox="0 0 24 14"><path d="M9 13 Q6 10 9 7 Q12 4 9 1 M15 13 Q12 10 15 7 Q18 4 15 1" fill="none" stroke="currentColor" stroke-width="1.5"/></symbol>
      <g id="step-row">
        <text x="28" y="30" fill="currentColor">1.</text>
        <use href="#icon-bowl" x="46" y="18" width="26" height="17"/>
        <text x="75" y="30" font-size="10" fill="currentColor">+</text>
        <use href="#icon-jug" x="86" y="11" width="21" height="25"/>
        <text x="150" y="30" fill="currentColor">2.</text>
        <use href="#icon-bowl" x="168" y="18" width="28" height="18"/>
        <use href="#icon-spoon" x="184" y="4" width="20" height="20"/>
        <text x="268" y="30" fill="currentColor">3.</text>
        <use href="#icon-bowl" x="290" y="18" width="28" height="18"/>
        <use href="#icon-steam" x="292" y="4" width="24" height="14"/>
        <line x1="22" y1="38" x2="352" y2="38" stroke="currentColor" stroke-width="1"/>
      </g>
      <g id="sweeps">
        <path d="M176 160 Q280 138 374 121 L374 129 Q280 146 176 161Z"/>
        <path d="M0 297 Q130 282 268 272 Q130 288 0 303Z"/>
      </g>
    </defs>
  </svg>

  <article class="label label--orange">
    <svg class="ribbon" viewBox="0 0 94 182" aria-hidden="true"><path d="M0 0H94V182L47 164L0 182Z"/></svg>
    <svg class="badge" viewBox="0 0 120 120" role="img" aria-label="Variety N°2: tripe, rice, vegetables">
      <circle class="disc" cx="60" cy="60" r="58"/>
      <circle class="ring" cx="60" cy="60" r="55"/>
      <circle class="ring" cx="60" cy="60" r="31"/>
      <text class="arc"><textPath href="#arc-top" startOffset="50%" text-anchor="middle">TRIPE, RICE</textPath></text>
      <text class="arc"><textPath href="#arc-bottom" startOffset="50%" text-anchor="middle">VEGETABLES</textPath></text>
      <text class="variety" x="60" y="70" text-anchor="middle">N°2</text>
    </svg>
    <p class="brand">Velderkamp</p>
    <svg class="sweep" viewBox="0 0 374 528" aria-hidden="true"><use href="#sweeps"/></svg>
    <h1 class="headline"><span class="main"><b>S</b>UPERB <b>F</b>RESH</span><span class="sub">Dog Food!</span></h1>
    <p class="because">Because ....</p>
    <div class="card" role="img" aria-label="Vintage taped card with a brown dog illustration and the hand-lettered quote: A Home without a dog is just a House"></div>
    <section class="band">
      <svg class="steps" viewBox="0 0 374 44" role="img" aria-label="Instructions: mix with hot water, wait, serve"><use href="#step-row"/></svg>
      <p class="instructions">Mengen met heet water, Vijf minuten wachten, klaar!</p>
    </section>
  </article>

  <article class="label label--crimson">
    <svg class="ribbon" viewBox="0 0 94 182" aria-hidden="true"><path d="M0 0H94V182L47 164L0 182Z"/></svg>
    <svg class="badge" viewBox="0 0 120 120" role="img" aria-label="Variety N°2: tripe, rice, vegetables">
      <circle class="disc" cx="60" cy="60" r="58"/>
      <circle class="ring" cx="60" cy="60" r="55"/>
      <circle class="ring" cx="60" cy="60" r="31"/>
      <text class="arc"><textPath href="#arc-top" startOffset="50%" text-anchor="middle">TRIPE, RICE</textPath></text>
      <text class="arc"><textPath href="#arc-bottom" startOffset="50%" text-anchor="middle">VEGETABLES</textPath></text>
      <text class="variety" x="60" y="70" text-anchor="middle">N°2</text>
    </svg>
    <p class="brand">Velderkamp</p>
    <svg class="sweep" viewBox="0 0 374 528" aria-hidden="true"><use href="#sweeps"/></svg>
    <h1 class="headline"><span class="main"><b>S</b>UPERB <b>F</b>RESH</span><span class="sub">Dog Food!</span></h1>
    <p class="because">Because ....</p>
    <div class="card" role="img" aria-label="Vintage taped card with a brown dog illustration and the hand-lettered quote: A Home without a dog is just a House"></div>
    <section class="band">
      <svg class="steps" viewBox="0 0 374 44" role="img" aria-label="Instructions: mix with hot water, wait, serve"><use href="#step-row"/></svg>
      <p class="instructions">Mengen met heet water, Vijf minuten wachten, klaar!</p>
    </section>
  </article>

  <article class="label label--teal">
    <svg class="ribbon" viewBox="0 0 94 182" aria-hidden="true"><path d="M0 0H94V182L47 164L0 182Z"/></svg>
    <svg class="badge" viewBox="0 0 120 120" role="img" aria-label="Variety N°3: tripe, rice, vegetables">
      <circle class="disc" cx="60" cy="60" r="58"/>
      <circle class="ring" cx="60" cy="60" r="55"/>
      <circle class="ring" cx="60" cy="60" r="31"/>
      <text class="arc"><textPath href="#arc-top" startOffset="50%" text-anchor="middle">TRIPE, RICE</textPath></text>
      <text class="arc"><textPath href="#arc-bottom" startOffset="50%" text-anchor="middle">VEGETABLES</textPath></text>
      <text class="variety" x="60" y="70" text-anchor="middle">N°3</text>
    </svg>
    <p class="brand">Velderkamp</p>
    <svg class="sweep" viewBox="0 0 374 528" aria-hidden="true"><use href="#sweeps"/></svg>
    <h1 class="headline"><span class="main"><b>S</b>UPERB <b>F</b>RESH</span><span class="sub">Dog Food!</span></h1>
    <p class="because">Because ....</p>
    <div class="card" role="img" aria-label="Vintage taped card with a brown dog illustration and the hand-lettered quote: A Home without a dog is just a House"></div>
    <section class="band">
      <svg class="steps" viewBox="0 0 374 44" role="img" aria-label="Instructions: mix with hot water, wait, serve"><use href="#step-row"/></svg>
      <p class="instructions">Mengen met heet water, Vijf minuten wachten, klaar!</p>
    </section>
  </article>

  <article class="label label--slate">
    <svg class="ribbon" viewBox="0 0 94 182" aria-hidden="true"><path d="M0 0H94V182L47 164L0 182Z"/></svg>
    <svg class="badge" viewBox="0 0 120 120" role="img" aria-label="Variety N°4: tripe, rice, vegetables">
      <circle class="disc" cx="60" cy="60" r="58"/>
      <circle class="ring" cx="60" cy="60" r="55"/>
      <circle class="ring" cx="60" cy="60" r="31"/>
      <text class="arc"><textPath href="#arc-top" startOffset="50%" text-anchor="middle">TRIPE, RICE</textPath></text>
      <text class="arc"><textPath href="#arc-bottom" startOffset="50%" text-anchor="middle">VEGETABLES</textPath></text>
      <text class="variety" x="60" y="70" text-anchor="middle">N°4</text>
    </svg>
    <p class="brand">Velderkamp</p>
    <svg class="sweep" viewBox="0 0 374 528" aria-hidden="true"><use href="#sweeps"/></svg>
    <h1 class="headline"><span class="main"><b>S</b>UPERB <b>F</b>RESH</span><span class="sub">Dog Food!</span></h1>
    <p class="because">Because ....</p>
    <div class="card" role="img" aria-label="Vintage taped card with a brown dog illustration and the hand-lettered quote: A Home without a dog is just a House"></div>
    <section class="band">
      <svg class="steps" viewBox="0 0 374 44" role="img" aria-label="Instructions: mix with hot water, wait, serve"><use href="#step-row"/></svg>
      <p class="instructions">Mengen met heet water, Vijf minuten wachten, klaar!</p>
    </section>
  </article>

  <article class="label label--paper">
    <svg class="ribbon" viewBox="0 0 94 182" aria-hidden="true"><path d="M0 0H94V182L47 164L0 182Z"/></svg>
    <svg class="badge" viewBox="0 0 120 120" role="img" aria-label="Variety N°5: tripe, rice, vegetables">
      <circle class="disc" cx="60" cy="60" r="58"/>
      <circle class="ring" cx="60" cy="60" r="55"/>
      <circle class="ring" cx="60" cy="60" r="31"/>
      <text class="arc"><textPath href="#arc-top" startOffset="50%" text-anchor="middle">TRIPE, RICE</textPath></text>
      <text class="arc"><textPath href="#arc-bottom" startOffset="50%" text-anchor="middle">VEGETABLES</textPath></text>
      <text class="variety" x="60" y="70" text-anchor="middle">N°5</text>
    </svg>
    <p class="brand">Velderkamp</p>
    <svg class="sweep" viewBox="0 0 374 528" aria-hidden="true"><use href="#sweeps"/></svg>
    <h1 class="headline"><span class="main"><b>S</b>UPERB <b>F</b>RESH</span><span class="sub">Dog Food!</span></h1>
    <p class="because">Because ....</p>
    <div class="card" role="img" aria-label="Vintage taped card with a brown dog illustration and the hand-lettered quote: A Home without a dog is just a House"></div>
    <section class="band">
      <svg class="steps" viewBox="0 0 374 44" role="img" aria-label="Instructions: mix with hot water, wait, serve"><use href="#step-row"/></svg>
      <p class="instructions">Mengen met heet water, Vijf minuten wachten, klaar!</p>
    </section>
  </article>

</main>
</body>
</html>
```